A professional oriented Health and Safety company is in need of a postcard design

Hello we need a postcard to draw business to our company Brisk Lantern LLC. We are a health and safety based company providing education and testing. The main focuses we offer are CPR and AED training for Health Care Providers and the general public, First Aid training, Bloodborne Pathogens training, and Respirator and N95 fit testing. We would like to see a professional looking postcard that reflects a lot on education. No cartoonist postcards please keep it crisp and clean. We have been in business since 2007 and can host large classes. We are educating and testing throughout the State of Michigan. Target audiences are Medical and Dental professionals, Child Care centers, Construction and Industrial. Please reference the telephone number and web site on the attached card and include in the postcard.

Some items we would like to see targeted in one way or another are as follows:
-We can train at the business inquiring making scheduling easy for all employees cutting overall costs. Off site training also available
-All training is by licensed healthcare providers
-We use clean and full functioning equipment with the latest technology available
-Pricing is typically lower than having to get educated at yearly conferences
-Courses meet State and OSHA requirements

We have attached some files with our current logo and a business card. We will consider projects with and without the logo. Please focus on the above not what's on the card.
Updates

Industry/Entity Type

Education

Requirements
Nice to have
• Pictures of Medical professionals

```html
<!DOCTYPE html>
<html lang="en">
<head>
<meta charset="utf-8">
<title>Brisk Lantern LLC Postcard</title>
<link rel="stylesheet" href="https://fonts.googleapis.com/css2?family=Lato:ital,wght@0,400;0,700;0,900;1,700&family=Oswald:wght@500&display=swap">
<style>
  :root {
    --page: #ece7e1;
    --red: #d8222a;
    --red-light: #ee4a4f;
    --red-deep: #a8101a;
    --ink: #1c1c1e;
    --ink-soft: #2b2b2e;
    --white: #ffffff;
    --grey: #bdbdbd;
    --photo-a: #e9d8cc;
    --photo-b: #b9c4d2;
  }
  * { box-sizing: border-box; margin: 0; padding: 0; }
  html, body { width: 902px; height: 1200px; overflow: hidden; }
  body { background: var(--page); font-family: "Lato", sans-serif; position: relative; }

  .postcard {
    position: absolute; left: 61px; width: 780px; height: 570px;
    overflow: hidden; background: var(--white);
    box-shadow: 0 6px 18px rgba(0,0,0,.28);
  }
  .postcard--front { top: 20px; }
  .postcard--back { top: 610px; }
  .postcard__art { position: absolute; inset: 0; width: 780px; height: 570px; }
  .postcard > *:not(svg) { position: absolute; }

  .headline {
    left: 34px; top: 14px; color: var(--white);
    font-weight: 900; font-size: 35px; line-height: 41px;
    text-shadow: 0 2px 3px rgba(0,0,0,.35);
  }
  .intro {
    left: 40px; top: 107px; color: var(--ink);
    font-weight: 700; font-size: 20px; line-height: 27px;
  }
  .pill {
    background: var(--ink); color: var(--white);
    font-weight: 900; font-size: 20px; height: 36px; line-height: 36px;
    padding-left: 40px; border-radius: 0 18px 18px 0; left: 0;
  }
  .pill--focus { top: 180px; width: 373px; }
  .pill--facilities { top: 140px; width: 220px; padding-left: 34px; }

  .focus-list { left: 40px; top: 228px; list-style: none; color: var(--white);
    font-style: italic; font-weight: 700; font-size: 16.5px; line-height: 20px; }
  .focus-list li { position: relative; padding-left: 32px; margin-bottom: 9.5px; }
  .focus-list svg { position: absolute; left: 0; top: 3px; width: 16px; height: 14px; }

  .badge {
    left: 283px; top: 317px; width: 136px; height: 136px; border-radius: 50%;
    background: var(--white); border: 5px solid var(--grey);
    box-shadow: 0 0 0 3px var(--white), 0 3px 8px rgba(0,0,0,.4);
    display: flex; align-items: center; justify-content: center; text-align: center;
    font-family: "Oswald", sans-serif; font-weight: 500; color: var(--red);
    font-size: 22px; line-height: 27px;
  }

  .brand-name { font-family: "Oswald", sans-serif; font-weight: 500; color: var(--red); font-size: 31px; line-height: 36px; }
  .postcard--front .brand-name { left: 42px; top: 444px; }
  .contact { display: flex; align-items: center; gap: 8px; font-weight: 700; font-size: 18.5px; color: var(--white); }
  .contact svg { width: 12px; height: 12px; flex: none; }
  .postcard--front .contact--phone { left: 42px; top: 498px; }
  .postcard--front .contact--email { left: 42px; top: 527px; }
  .postcard--front .contact--web { left: 306px; top: 527px; }

  .back-name { left: 28px; top: 16px; font-family: "Oswald", sans-serif; font-weight: 500; font-size: 28px; line-height: 34px; color: var(--ink); }
  .back-intro { left: 33px; top: 53px; color: var(--white); font-weight: 700; font-size: 18.5px; line-height: 25.5px; }
  .facility-list { left: 30px; top: 190px; width: 370px; list-style: none; color: var(--white); font-size: 14.5px; line-height: 19px; }
  .facility-list li { position: relative; padding-left: 28px; margin-bottom: 10px; }
  .facility-list svg { position: absolute; left: 0; top: 3px; width: 14px; height: 12px; }

  .stamp-box { left: 677px; top: 40px; width: 84px; height: 100px; border: 2px solid var(--ink-soft); }
  .address-line { left: 512px; width: 248px; height: 2px; background: var(--ink-soft); }
  .address-line--1 { top: 326px; }
  .address-line--2 { top: 371px; }
  .address-line--3 { top: 414px; }

  .postcard--back .brand-name { left: 33px; top: 494px; font-size: 28px; }
  .postcard--back .contact { color: var(--ink); font-size: 18px; }
  .postcard--back .contact--web { left: 33px; top: 533px; }
  .postcard--back .contact--phone { left: 273px; top: 505px; }
  .postcard--back .contact--email { left: 273px; top: 534px; }
</style>
</head>
<body>

<svg width="0" height="0" style="position:absolute">
  <defs>
    <radialGradient id="redField" cx="30%" cy="30%" r="80%">
      <stop offset="0" stop-color="#ee4a4f"/>
      <stop offset="1" stop-color="#b8121b"/>
    </radialGradient>
    <linearGradient id="darkField" x1="0" y1="0" x2="0" y2="1">
      <stop offset="0" stop-color="#2b2b2e"/>
      <stop offset="1" stop-color="#141416"/>
    </linearGradient>
    <linearGradient id="photoTone" x1="0" y1="0" x2="1" y2="1">
      <stop offset="0" stop-color="#e9d8cc"/>
      <stop offset=".55" stop-color="#e8b27c"/>
      <stop offset="1" stop-color="#b9c4d2"/>
    </linearGradient>
    <symbol id="icon-heart" viewBox="0 0 16 14"><path d="M8 13.5 1.5 7.2A3.9 3.9 0 0 1 8 2.3a3.9 3.9 0 0 1 6.5 4.9Z" fill="#2a0b0d"/><path d="M3 7h3l1-2 2 4 1-2h3" stroke="#fff" stroke-width="1.2" fill="none"/></symbol>
    <symbol id="icon-tick" viewBox="0 0 14 12"><path d="M1 6.5 5 10.5 13 1.5" stroke="#1c1c1e" stroke-width="2.6" fill="none" stroke-linecap="round" stroke-linejoin="round"/></symbol>
    <symbol id="icon-phone" viewBox="0 0 12 12"><path d="M3 .5 5 3 3.8 4.4a7 7 0 0 0 3.8 3.8L9 7l2.5 2-1.3 2.3C5.5 11 1 6.5.7 1.8Z" fill="#d8222a"/></symbol>
    <symbol id="icon-mail" viewBox="0 0 12 12"><rect x=".5" y="2.5" width="11" height="7" fill="#d8222a"/><path d="M.5 2.5 6 7l5.5-4.5" stroke="#fff" stroke-width="1" fill="none"/></symbol>
    <symbol id="icon-globe" viewBox="0 0 12 12"><circle cx="6" cy="6" r="5.5" fill="#d8222a"/><path d="M.5 6h11M6 .5c-3 3-3 8 0 11M6 .5c3 3 3 8 0 11" stroke="#fff" stroke-width=".8" fill="none"/></symbol>
  </defs>
</svg>

<section class="postcard postcard--front">
  <svg class="postcard__art" viewBox="0 0 780 570" aria-hidden="true">
    <rect width="780" height="570" fill="url(#redField)"/>
    <path d="M0 420 C150 455 300 458 440 448 L780 470 L780 570 L0 570 Z" fill="url(#darkField)"/>
    <path d="M0 404 C150 440 300 446 440 436" stroke="#fff" stroke-width="9" fill="none"/>
    <path d="M0 415 C150 451 300 456 440 446" stroke="#1c1c1e" stroke-width="6" fill="none"/>
    <path d="M780 46 C590 54 410 180 394 330 C384 425 432 482 540 488 L780 488 Z" fill="#1c1c1e"/>
    <path d="M780 54 C598 64 418 186 402 330 C393 420 440 474 540 480 L780 480 Z" fill="#fff"/>
  </svg>
  <svg class="postcard__art" viewBox="0 0 780 570" role="img" aria-label="Photo of two healthcare instructors practising chest compressions on a CPR training manikin">
    <path d="M780 64 C606 74 428 192 412 330 C404 414 448 466 540 472 L780 472 Z" fill="url(#photoTone)"/>
  </svg>

  <h1 class="headline">Servicing your&nbsp; community needs<br>to our full capabilities</h1>
  <p class="intro">We are a health and safety based company<br>providing education and testing.</p>
  <div class="pill pill--focus">The main focuses we offer</div>
  <ul class="focus-list">
    <li><svg><use href="#icon-heart"/></svg>CPR and AED training for Health Care<br>Providers and the general public</li>
    <li><svg><use href="#icon-heart"/></svg>First Aid training &amp; Bloodborne</li>
    <li><svg><use href="#icon-heart"/></svg>Pathogens training</li>
    <li><svg><use href="#icon-heart"/></svg>N95 fit testing</li>
    <li><svg><use href="#icon-heart"/></svg>Respirator</li>
  </ul>
  <div class="badge">Book Your<br>Appoinment<br>Now</div>

  <div class="brand-name">Brisk Lantern LLC</div>
  <div class="contact contact--phone"><svg><use href="#icon-phone"/></svg>(555)014-2290</div>
  <div class="contact contact--email"><svg><use href="#icon-mail"/></svg>info@brisklantern.org</div>
  <div class="contact contact--web"><svg><use href="#icon-globe"/></svg>www.brisklantern.org</div>
</section>

<section class="postcard postcard--back">
  <svg class="postcard__art" viewBox="0 0 780 570" aria-hidden="true">
    <path d="M0 0 L594 0 C578 130 540 300 440 392 C340 478 160 488 0 480 Z" fill="#1c1c1e"/>
    <path d="M0 0 L584 0 C568 128 530 294 432 384 C334 468 160 476 0 468 Z" fill="#fff"/>
    <path d="M0 0 L576 0 C560 126 522 290 426 378 C330 460 160 468 0 460 Z" fill="url(#redField)"/>
  </svg>

  <div class="back-name">Brisk Lantern LLC</div>
  <p class="back-intro">Since 2007 Brisk Lantern has been servicing<br>your&nbsp; community needs to our full<br>capabilities.</p>
  <div class="pill pill--facilities">Our Facilities</div>
  <ul class="facility-list">
    <li><svg><use href="#icon-tick"/></svg>We can train at the business inquiring making scheduling easy for all employees cutting overall costs. Off site training also available</li>
    <li><svg><use href="#icon-tick"/></svg>Courses meet State and OSHA requirements</li>
    <li><svg><use href="#icon-tick"/></svg>Pricing is typically lower than having to<br>get educated at yearly conferences</li>
    <li><svg><use href="#icon-tick"/></svg>All training is by licensed healthcare<br>providers</li>
    <li><svg><use href="#icon-tick"/></svg>We use clean and full functioning<br>equipment with the latest<br>technology available</li>
  </ul>

  <div class="stamp-box"></div>
  <div class="address-line address-line--1"></div>
  <div class="address-line address-line--2"></div>
  <div class="address-line address-line--3"></div>

  <div class="brand-name">Brisk Lantern LLC</div>
  <div class="contact contact--web"><svg><use href="#icon-globe"/></svg>www.brisklantern.org</div>
  <div class="contact contact--phone"><svg><use href="#icon-phone"/></svg>(555)014-2290</div>
  <div class="contact contact--email"><svg><use href="#icon-mail"/></svg>info@brisklantern.org</div>
</section>

</body>
</html>
```